PowerPoint Template for our Business

We are looking for a professional and visually appealing PowerPoint template for our business, Pellion Labs. We specialize in calibration services and are currently undergoing a rebranding process. The new template should align with our updated brand identity, using the provided color palette and logos.
Project Requirements:
Title Slide:
Full Pellion Labs logo prominently displayed.
Clean and professional layout.
Background color should be white with brand accents.
Title and subtitle areas clearly defined.
Content Slide:
Consistent use of brand colors for headers, footers, and other elements.
Space for text, images, charts, and graphs.
PX logo subtly incorporated.
Clean and modern layout ensuring readability and professionalism.
Section Header Slide:
Clear differentiation from content slides.
Use of PX logo and brand color for background.
Professional typography.
Closing Slide:
Full Pellion Labs logo with a final message.
Clean background, professional layout.
Space for a thank you message and contact information.
Brand Colors:
Green: RGB (207, 255, 0)
Light Gray: RGB (239, 239, 239)
Gray: RGB (191, 191, 191)
Black: RGB (0, 0, 0)
White: RGB (255, 255, 255)
Deliverables:
A fully editable PowerPoint template (.pptx format).
Fonts and any additional assets used in the design.
Additional Information:
Please refer to the attached logos and color palette for guidance.
We are looking for a design that is not only professional and visually appealing but also functional for business presentations.
We look forward to seeing your creative proposals and selecting a design that best represents our brand.
Thank you!

```html
<!DOCTYPE html>
<html lang="en">
<head>
<meta charset="utf-8">
<title>Pellion Labs – Presentation Template</title>
<link rel="stylesheet" href="https://fonts.googleapis.com/css2?family=Poppins:wght@400;500;600;800&display=swap">
<style>
:root{
  --green:#cfff00;
  --light-gray:#efefef;
  --gray:#bfbfbf;
  --mid-gray:#8c8c8c;
  --dark-gray:#5a5a5a;
  --black:#000000;
  --ink:#1a1a1a;
  --white:#ffffff;
}
*{box-sizing:border-box;margin:0;padding:0}
html,body{width:1200px;height:3643px;overflow:hidden}
body{background:var(--light-gray);font-family:"Poppins",sans-serif;color:var(--ink);position:relative}
.slide{position:absolute;left:99px;width:1002px;height:562px;background:var(--white);overflow:hidden}
.abs{position:absolute}
.green{background:var(--green)}
.title-bar{position:absolute;left:17px;top:42px;width:8px;height:64px;background:var(--mid-gray)}
.slide-title{position:absolute;left:42px;top:34px;font-size:35px;line-height:38px;font-weight:400;color:var(--black)}
.slide-title strong{font-weight:800}
.body-text{font-size:17.5px;line-height:31px;color:#333}
.footer{position:absolute;left:0;top:514px;width:1002px;height:48px;background:var(--black);display:flex;align-items:center;padding:0 17px}
.footer-brand{display:flex;align-items:center;gap:10px;color:var(--white);font-size:13px;font-weight:500}
.brand-square{width:20px;height:20px;background:var(--green)}
.page-num{margin-left:auto;width:28px;height:28px;border-radius:50%;background:var(--green);color:var(--black);font-size:12px;font-weight:600;display:flex;align-items:center;justify-content:center}
.photo{position:absolute}
/* slide 1 */
.hero-title{position:absolute;left:24px;top:160px;font-size:45px;line-height:52px;color:var(--black);font-weight:800;letter-spacing:1px}
.hero-title .light{font-weight:400}
.hero-sub{position:absolute;left:24px;top:287px;width:440px;font-size:19.5px;line-height:31.5px;font-weight:500;color:#222}
/* slide 3 */
.lead{position:absolute;left:344px;top:18px;width:400px;font-size:20px;line-height:31px;font-weight:500;color:var(--black)}
.card{position:absolute;top:155px;width:307px;height:335px;background:var(--white);box-shadow:0 2px 10px rgba(0,0,0,.12);padding:24px 20px}
.card-icon{width:92px;height:86px}
.card-title{margin-top:30px;font-size:23px;font-weight:800;color:var(--black)}
.check-list{list-style:none;margin-top:14px}
.check-list li{display:flex;align-items:center;gap:12px;font-size:15.5px;height:35.5px;color:#333}
.check-dot{width:16px;height:16px;flex:none}
/* slide 5 */
.chart{position:absolute;left:0;top:120px}
.chart-copy{position:absolute;left:519px;top:158px;width:470px}
.chart-copy p{font-size:16.5px;line-height:27px;font-weight:500;color:#333}
.tick-list{list-style:none;margin-top:18px}
.tick-list li{display:flex;gap:14px;font-size:16px;line-height:26px;color:#444;margin-bottom:15px}
.tick-list svg{flex:none;margin-top:6px}
/* slide 6 */
.closing{background:linear-gradient(135deg,#fbfbfb,#f1f1f1)}
.contact-card{position:absolute;left:42px;top:64px;width:426px;height:427px;background:var(--white);padding:36px 26px}
.thanks{font-size:46px;line-height:54px;font-weight:400;color:var(--black);letter-spacing:1px}
.thanks strong{font-weight:800}
.contact-card .intro{margin-top:14px;font-size:17.5px;line-height:27px;color:#333}
.contact-row{display:flex;align-items:center;gap:22px;margin-top:20px;font-size:18px;line-height:27px;color:#222}
.contact-row:first-of-type{margin-top:34px}
.contact-icon{width:44px;height:44px;border:2px solid var(--black);border-radius:50%;display:flex;align-items:center;justify-content:center;flex:none}
.closing-brand{position:absolute;left:539px;top:237px;display:flex;align-items:center;gap:22px}
.closing-brand .mark{width:95px;height:92px;background:var(--black)}
.closing-brand span{font-size:41px;font-weight:400;color:var(--black)}
</style>
</head>
<body>

<!-- Title slide -->
<section class="slide" style="top:57px">
  <div class="abs green" style="left:24px;top:0;width:79px;height:117px"></div>
  <h1 class="hero-title"><span>Welcome to</span><br><span class="light">Pellion</span> Labs</h1>
  <p class="hero-sub">Excepteur sint occaecat cupidatat non proident, sunt in culpa qui officia deserunt mollit anim id est laborum</p>
  <div class="abs green" style="left:1px;top:480px;width:253px;height:47px"></div>
  <div class="photo" role="img" aria-label="Technician calibrating a dial gauge on a precision test stand" style="left:419px;top:24px;width:583px;height:515px;background:linear-gradient(135deg,#8a8f96,#4d5258 55%,#2f3338)"></div>
</section>

<!-- Content slide: text + image -->
<section class="slide" style="top:648px">
  <div class="title-bar"></div>
  <h2 class="slide-title">Excepteur Sint<br><strong>Occaecat</strong></h2>
  <p class="abs body-text" style="left:42px;top:140px;width:430px">Sed ut perspiciatis unde omnis iste natus error sit voluptatem accusantium doloremque laudantium, totam rem aperiam, eaque ipsa quae ab illo inventore veritatis et quasi architecto beatae vitae dicta sunt explicabo. Nemo enim ipsam voluptatem quia voluptas sit aspernatur aut odit aut fugit, sed quia cons equuntur magni dolores eos qui ratione voluptatem sequi nesciunteque porro quisquam est.</p>
  <div class="abs green" style="left:899px;top:0;width:103px;height:514px"></div>
  <div class="abs" style="left:515px;top:417px;width:89px;height:85px;background:var(--mid-gray)"></div>
  <div class="photo" role="img" aria-label="Handheld multimeter probing an electronics board in a lab" style="left:533px;top:42px;width:428px;height:437px;background:linear-gradient(160deg,#5fa8e0,#2c7fd0 50%,#d9dde2)"></div>
  <footer class="footer"><div class="footer-brand"><span class="brand-square"></span>PellionLabs</div><span class="page-num">2</span></footer>
</section>

<!-- Content slide: three cards -->
<section class="slide" style="top:1242px">
  <div class="title-bar"></div>
  <h2 class="slide-title">Excepteur Sint<br><strong>Occaecat</strong></h2>
  <p class="lead">Nemo enim ipsam voluptatem aspernatur aut odit aut fugit, sed q uia consequuntur</p>
  <div class="abs green" style="left:746px;top:37px;width:256px;height:47px"></div>

  <div class="card" style="left:13px">
    <svg class="card-icon" viewBox="0 0 92 86" fill="none" stroke="#000" stroke-width="2.5"><rect x="4" y="4" width="84" height="58" rx="2"/><line x1="4" y1="52" x2="88" y2="52"/><line x1="46" y1="62" x2="46" y2="74"/><line x1="28" y1="76" x2="64" y2="76"/><circle cx="28" cy="28" r="16"/><line x1="12" y1="28" x2="44" y2="28"/><line x1="28" y1="12" x2="28" y2="44"/><line x1="54" y1="16" x2="80" y2="16"/><line x1="54" y1="28" x2="80" y2="28"/><line x1="54" y1="40" x2="80" y2="40"/></svg>
    <h3 class="card-title">Quis autem vel eum</h3>
    <ul class="check-list">
      <li><svg class="check-dot" viewBox="0 0 16 16"><circle cx="8" cy="8" r="8" fill="#222"/><path d="M4.5 8.2l2.3 2.3 4.7-4.7" stroke="#fff" stroke-width="1.8" fill="none"/></svg>Sed ut perspiciatis unde omnis</li>
      <li><svg class="check-dot" viewBox="0 0 16 16"><circle cx="8" cy="8" r="8" fill="#222"/><path d="M4.5 8.2l2.3 2.3 4.7-4.7" stroke="#fff" stroke-width="1.8" fill="none"/></svg>Sed ut perspiciatis unde</li>
      <li><svg class="check-dot" viewBox="0 0 16 16"><circle cx="8" cy="8" r="8" fill="#222"/><path d="M4.5 8.2l2.3 2.3 4.7-4.7" stroke="#fff" stroke-width="1.8" fill="none"/></svg>Rem aperiam</li>
      <li><svg class="check-dot" viewBox="0 0 16 16"><circle cx="8" cy="8" r="8" fill="#222"/><path d="M4.5 8.2l2.3 2.3 4.7-4.7" stroke="#fff" stroke-width="1.8" fill="none"/></svg>Sed ut perspiciatis unde</li>
    </ul>
  </div>

  <div class="card" style="left:347px">
    <svg class="card-icon" viewBox="0 0 92 86" fill="none" stroke="#000" stroke-width="2.5"><rect x="4" y="4" width="72" height="54" rx="4"/><rect x="12" y="10" width="56" height="22"/><path d="M16 24l8-8 8 10 8-8 8 8 8-6 8 6"/><circle cx="18" cy="44" r="6"/><circle cx="34" cy="44" r="6"/><line x1="48" y1="42" x2="68" y2="42"/><line x1="48" y1="48" x2="68" y2="48"/><path d="M76 50h10v24H40"/><rect x="16" y="68" width="24" height="12"/></svg>
    <h3 class="card-title">Quis autem vel eum</h3>
    <ul class="check-list">
      <li><svg class="check-dot" viewBox="0 0 16 16"><circle cx="8" cy="8" r="8" fill="#222"/><path d="M4.5 8.2l2.3 2.3 4.7-4.7" stroke="#fff" stroke-width="1.8" fill="none"/></svg>Sed ut perspiciatis unde omnis</li>
      <li><svg class="check-dot" viewBox="0 0 16 16"><circle cx="8" cy="8" r="8" fill="#222"/><path d="M4.5 8.2l2.3 2.3 4.7-4.7" stroke="#fff" stroke-width="1.8" fill="none"/></svg>Sed ut perspiciatis unde</li>
      <li><svg class="check-dot" viewBox="0 0 16 16"><circle cx="8" cy="8" r="8" fill="#222"/><path d="M4.5 8.2l2.3 2.3 4.7-4.7" stroke="#fff" stroke-width="1.8" fill="none"/></svg>Rem aperiam</li>
      <li><svg class="check-dot" viewBox="0 0 16 16"><circle cx="8" cy="8" r="8" fill="#222"/><path d="M4.5 8.2l2.3 2.3 4.7-4.7" stroke="#fff" stroke-width="1.8" fill="none"/></svg>Sed ut perspiciatis unde</li>
    </ul>
  </div>

  <div class="card" style="left:681px">
    <svg class="card-icon" viewBox="0 0 92 86" fill="none" stroke="#000" stroke-width="2.5"><circle cx="24" cy="14" r="5"/><path d="M21 19L8 64M27 19l13 45"/><line x1="12" y1="44" x2="36" y2="44"/><circle cx="62" cy="24" r="14"/><circle cx="62" cy="24" r="5"/><line x1="62" y1="38" x2="62" y2="64"/><rect x="4" y="66" width="84" height="12"/><line x1="20" y1="66" x2="20" y2="72"/><line x1="36" y1="66" x2="36" y2="72"/><line x1="52" y1="66" x2="52" y2="72"/><line x1="68" y1="66" x2="68" y2="72"/></svg>
    <h3 class="card-title">Quis autem vel eum</h3>
    <ul class="check-list">
      <li><svg class="check-dot" viewBox="0 0 16 16"><circle cx="8" cy="8" r="8" fill="#222"/><path d="M4.5 8.2l2.3 2.3 4.7-4.7" stroke="#fff" stroke-width="1.8" fill="none"/></svg>Sed ut perspiciatis unde omnis</li>
      <li><svg class="check-dot" viewBox="0 0 16 16"><circle cx="8" cy="8" r="8" fill="#222"/><path d="M4.5 8.2l2.3 2.3 4.7-4.7" stroke="#fff" stroke-width="1.8" fill="none"/></svg>Sed ut perspiciatis unde</li>
      <li><svg class="check-dot" viewBox="0 0 16 16"><circle cx="8" cy="8" r="8" fill="#222"/><path d="M4.5 8.2l2.3 2.3 4.7-4.7" stroke="#fff" stroke-width="1.8" fill="none"/></svg>Rem aperiam</li>
      <li><svg class="check-dot" viewBox="0 0 16 16"><circle cx="8" cy="8" r="8" fill="#222"/><path d="M4.5 8.2l2.3 2.3 4.7-4.7" stroke="#fff" stroke-width="1.8" fill="none"/></svg>Sed ut perspiciatis unde</li>
    </ul>
  </div>
  <footer class="footer"><div class="footer-brand"><span class="brand-square"></span>PellionLabs</div><span class="page-num">3</span></footer>
</section>

<!-- Content slide: text + large image -->
<section class="slide" style="top:1836px">
  <div class="title-bar"></div>
  <h2 class="slide-title">Excepteur Sint<br><strong>Occaecat</strong></h2>
  <p class="abs body-text" style="left:41px;top:114px;width:400px">Nemo enim ipsam voluptatem quia voluptas sit aspernatur aut odit aut fugit, sed quia consequuntur magni dolores eos qui ratione voluptatem sequi nesciunteque porro quisquam est, qui dolorem ipsum quia dolor sit amet, consectetur, adipisci velit, sed quia non numquam eius modi tempora incidunt ut labore et dolore magnam aliquam quaerat voluptatem.</p>
  <div class="abs green" style="left:20px;top:402px;width:47px;height:112px"></div>
  <div class="photo" role="img" aria-label="Gloved hands adjusting a precision micrometer" style="left:443px;top:0;width:559px;height:514px;background:linear-gradient(140deg,#c9d6ec,#6f8fc4 50%,#34487a)"></div>
  <footer class="footer"><div class="footer-brand"><span class="brand-square"></span>PellionLabs</div><span class="page-num">4</span></footer>
</section>

<!-- Content slide: chart -->
<section class="slide" style="top:2435px">
  <div class="title-bar" style="top:24px;height:58px"></div>
  <h2 class="slide-title" style="top:30px">Excepteur Sint <strong>Occaecat</strong></h2>
  <div class="abs green" style="left:746px;top:31px;width:256px;height:47px"></div>
  <svg class="chart" width="500" height="400" viewBox="0 0 500 400" font-family="Poppins, sans-serif" font-size="9" fill="#444">
    <g text-anchor="end">
      <text x="43" y="22">100%</text><text x="43" y="56">90%</text><text x="43" y="90">80%</text><text x="43" y="124">70%</text><text x="43" y="157">60%</text><text x="43" y="191">50%</text><text x="43" y="225">40%</text><text x="43" y="259">30%</text><text x="43" y="292">20%</text><text x="43" y="326">10%</text><text x="43" y="360">0%</text>
    </g>
    <line x1="50" y1="357" x2="495" y2="357" stroke="#ccc"/>
    <g fill="#cfff00">
      <rect x="65" y="137" width="19" height="220"/>
      <rect x="125" y="171" width="19" height="186"/>
      <rect x="186" y="53" width="19" height="304"/>
      <rect x="246" y="181" width="19" height="176"/>
      <rect x="307" y="249" width="19" height="108"/>
      <rect x="368" y="103" width="19" height="254"/>
      <rect x="429" y="22" width="19" height="335"/>
    </g>
    <g fill="#5a5a5a">
      <rect x="84" y="222" width="19" height="135"/>
      <rect x="144" y="80" width="19" height="277"/>
      <rect x="205" y="279" width="19" height="78"/>
      <rect x="265" y="222" width="19" height="135"/>
      <rect x="326" y="191" width="19" height="166"/>
      <rect x="387" y="137" width="19" height="220"/>
      <rect x="448" y="320" width="19" height="37"/>
    </g>
    <g text-anchor="middle">
      <text x="84" y="375">2018</text><text x="144" y="375">2019</text><text x="205" y="375">2020</text><text x="265" y="375">2021</text><text x="326" y="375">2022</text><text x="387" y="375">2023</text><text x="448" y="375">2024</text>
    </g>
  </svg>
  <div class="chart-copy">
    <p>Sed ut perspiciatis unde omnis iste natus erroluptatem accusantium doloremque laudantium, totam rem aperiam, eaque ipsa quae ab illo.</p>
    <ul class="tick-list">
      <li><svg width="15" height="12" viewBox="0 0 15 12"><path d="M1 6l4.5 4.5L14 1.5" stroke="#000" stroke-width="2.4" fill="none"/></svg>Sed ut perspiciatis unde omnis iste natus error sit</li>
      <li><svg width="15" height="12" viewBox="0 0 15 12"><path d="M1 6l4.5 4.5L14 1.5" stroke="#000" stroke-width="2.4" fill="none"/></svg>Voluptatem accusantium doloremque laudantium, totam rem aperiam, eaque ipsa quae ab illo.</li>
      <li><svg width="15" height="12" viewBox="0 0 15 12"><path d="M1 6l4.5 4.5L14 1.5" stroke="#000" stroke-width="2.4" fill="none"/></svg>Inventore veritatis et quasi architecto beatae</li>
      <li><svg width="15" height="12" viewBox="0 0 15 12"><path d="M1 6l4.5 4.5L14 1.5" stroke="#000" stroke-width="2.4" fill="none"/></svg>Vitae dicta sunt explicabo.</li>
    </ul>
  </div>
  <footer class="footer"><div class="footer-brand"><span class="brand-square"></span>PellionLabs</div><span class="page-num">5</span></footer>
</section>

<!-- Closing slide -->
<section class="slide closing" style="top:3033px">
  <div class="abs green" style="left:0;top:0;width:103px;height:562px"></div>
  <div class="abs" style="left:396px;top:431px;width:89px;height:86px;background:var(--mid-gray)"></div>
  <div class="contact-card">
    <h2 class="thanks">Thank <strong>You</strong></h2>
    <p class="intro">Excepteur sint occaecat cupidatat non proident, sunt in culpa qui officia deseru nt mollit anim id est laborum</p>
    <div class="contact-row"><span class="contact-icon"><svg width="20" height="20" viewBox="0 0 20 20" fill="none" stroke="#000" stroke-width="1.8"><circle cx="10" cy="10" r="8"/><ellipse cx="10" cy="10" rx="3.5" ry="8"/><line x1="2" y1="10" x2="18" y2="10"/></svg></span><span>48 Harbor Lane Suite 210,<br>Denver 80202, United States</span></div>
    <div class="contact-row"><span class="contact-icon"><svg width="20" height="20" viewBox="0 0 20 20"><path d="M5 2l3 4-2 2c1 2.5 3.5 5 6 6l2-2 4 3-2 3C9 18 2 11 2 4z" fill="none" stroke="#000" stroke-width="1.8"/></svg></span><span>+1-555-014-2290</span></div>
    <div class="contact-row"><span class="contact-icon"><svg width="20" height="16" viewBox="0 0 20 16"><rect x="1" y="1" width="18" height="14" rx="2" fill="#000"/><path d="M2 3l8 6 8-6" stroke="#fff" stroke-width="1.6" fill="none"/></svg></span><span>hello@pellionlabs.com</span></div>
  </div>
  <div class="closing-brand"><span class="mark"></span><span>PellionLabs</span></div>
  <div class="abs green" style="left:877px;top:347px;width:95px;height:215px"></div>
</section>

</body>
</html>
```